Book Cover for Lanterns Beyond the Quiet Tide

I need a book cover for a 6 x 9 paperback titled Lanterns Beyond the Quiet Tide Told by Scholars and Souls Dwelling in the Realm past Our Realm. It has to do with consciousness, the mind, incarnation onto Earth, leaving Earth, and the life in the life after this life. I have an idea I'm providing with this description, but I am open to anything that would be striking and stimulating, whether with a book or not. I am the author, T. Dwight Falmer. I've added another background idea to see if anyone can do something with it and I've increased the budget.

```html
<!DOCTYPE html>
<html lang="en">
<head>
<meta charset="utf-8">
<title>Lanterns Beyond the Quiet Tide — Book Cover</title>
<link rel="stylesheet" href="https://fonts.googleapis.com/css2?family=Tinos:wght@400&display=swap">
<style>
  :root {
    --stage-light: #8a8a8c;
    --stage-dark: #6c6c6e;
    --space-deep: #15112f;
    --space-mid: #2b1a3a;
    --glow-core: #f6b27a;
    --glow-warm: #d0602e;
    --glow-red: #7a2430;
    --ink-white: #ffffff;
  }
  * { margin: 0; padding: 0; box-sizing: border-box; }
  html, body {
    width: 1200px;
    height: 1200px;
    overflow: hidden;
  }
  body {
    background: radial-gradient(ellipse at 50% 40%, var(--stage-light), var(--stage-dark));
    position: relative;
    font-family: "Tinos", "Times New Roman", serif;
  }
  .book-cover {
    position: absolute;
    left: 340px;
    top: 205px;
    width: 520px;
    height: 790px;
    overflow: hidden;
    box-shadow: 0 10px 30px rgba(0,0,0,0.35);
  }
  .cover-art {
    position: absolute;
    inset: 0;
    background: radial-gradient(ellipse 60% 48% at 50% 60%, var(--glow-core) 0%, var(--glow-warm) 30%, var(--glow-red) 60%, var(--space-mid) 82%, var(--space-deep) 100%);
  }
  .title {
    position: absolute;
    top: 86px;
    left: 0;
    right: 0;
    text-align: center;
    color: var(--ink-white);
    font-size: 58px;
    line-height: 0.9;
    font-weight: 400;
    text-transform: uppercase;
    text-shadow: 0 2px 4px rgba(0,0,0,0.5);
  }
  .title span { display: block; }
  .subtitle {
    position: absolute;
    top: 652px;
    left: 0;
    right: 0;
    text-align: center;
    color: var(--ink-white);
    font-size: 17px;
    line-height: 1.2;
  }
  .author {
    position: absolute;
    top: 722px;
    left: 0;
    right: 0;
    text-align: center;
    color: var(--ink-white);
    font-size: 36px;
    font-weight: 400;
  }
</style>
</head>
<body>
  <main class="book-cover">
    <div class="cover-art" role="img" aria-label="Cover illustration: deep space with warm light rising behind Earth's horizon, a white question mark shaped like a head in profile with a small globe as its dot"></div>

    <h1 class="title">
      <span>Lanterns</span>
      <span>Beyond</span>
      <span>the Quiet</span>
      <span>Tide</span>
    </h1>

    <p class="subtitle">Told by Scholars and Souls Dwelling<br>in the Realm past Our Realm</p>

    <p class="author">T. Dwight Falmer</p>
  </main>
</body>
</html>
```